LustPrep.com 350x250 Creative Banner Ad & Logo **

UPDATE: For inspiration, please see new images attached. Also, please visit the following link to understand what our website niche will be about:

https://m.vidhollow.example/watch?v=Qk3TpaLx8Rn&feature=vidhol.example

We need several creative banner ad's (350x250) for various PornSites based on 3 themes; gay, straight and multiracial. Winning designers should have proven record of successful clickthrough conversions. Our website; LustPrep.com will offer 20,000 adult novelty products, BUT we want to position ourselves as the go to provider for premium Grooming and Shaving products - hence the name LustPrep.... We also need a new Logo for our website and other marketing materials (see attached). Unfortunately, this is the best we could do on our own and does not at this point represent the brand image we are looking for. We are looking for more creative ideas..

Target Market(s)

Adult Males 80%, Adult Females 20%

Logo Text

LustPrep.com - Set for Whatever!

Requirements
Must have
• From designer with proven track record of high click through success rates. Designs should be creative and help establish a brand image. Three (3) themes; gay, straight, multiracial. We are open to suggestions. Ads will be displayed on the big 3 porn sites through velvet routing - so must be in .jpg format and compatable with all devices.
Nice to have
• Multiple design options
New and creative ideas
Should not have
• We are paying for custom design service and do not want anything that looks and feels like a standard template or "off-the-shelf" design.. We expect to be "Wowed!".

```html
<!DOCTYPE html>
<html lang="en">
<head>
<meta charset="utf-8">
<title>LustPrep.com – Banner Options</title>
<link rel="stylesheet" href="https://fonts.googleapis.com/css2?family=Poppins:wght@500;600;700&family=Kaushan+Script&display=swap">
<style>
  :root {
    --backdrop: #cfcfcf;
    --paper: #ffffff;
    --paper-grey: #ebebeb;
    --ink: #141414;
    --pink: #f4306f;
    --peach: #f7a47e;
    --shadow-grey: #b9b9b9;
    --skin: #c79a84;
    --skin-dark: #6d4b3e;
    --tool: #1d1d1d;
  }
  * { margin: 0; padding: 0; box-sizing: border-box; }
  html, body {
    width: 1200px; height: 459px; overflow: hidden;
    background: var(--backdrop);
    font-family: "Poppins", sans-serif;
  }
  .banner {
    position: absolute; top: 48px;
    width: 509px; height: 366px; overflow: hidden;
    box-shadow: 6px 8px 10px rgba(0,0,0,0.35);
  }
  .banner--dark { left: 52px; background: var(--paper-grey); }
  .banner--light { left: 619px; background: var(--paper); }
  .banner__art { position: absolute; inset: 0; }

  .brand { position: absolute; color: var(--ink); }
  .brand__name { font-weight: 700; font-size: 27px; line-height: 1; letter-spacing: 0.3px; }
  .brand__tagline { font-weight: 500; font-size: 12px; margin-top: 6px; margin-left: 26px; }
  .banner--dark .brand { left: 23px; top: 44px; }
  .banner--light .brand { left: 38px; top: 50px; }

  .cta {
    position: absolute; display: flex; align-items: center; justify-content: center;
    color: var(--paper); font-weight: 600; font-size: 14px; letter-spacing: 0.8px;
    background: linear-gradient(90deg, var(--pink), var(--peach));
  }
  .banner--dark .cta {
    left: 26px; top: 174px; width: 125px; height: 44px;
    box-shadow: 3px 3px 0 var(--ink);
  }
  .banner--light .cta {
    left: 38px; top: 274px; width: 128px; height: 42px; border-radius: 21px;
  }

  .headline { position: absolute; left: 38px; top: 168px; color: var(--ink); }
  .headline__row { display: flex; align-items: center; gap: 10px; }
  .headline__key {
    background: var(--ink); color: var(--pink);
    font-weight: 500; font-size: 25px; line-height: 32px; padding: 0 10px;
  }
  .headline__script { font-family: "Kaushan Script", cursive; font-size: 27px; line-height: 1.2; }
</style>
</head>
<body>

<section class="banner banner--dark">
  <svg class="banner__art" width="509" height="366" viewBox="0 0 509 366">
    <defs>
      <linearGradient id="ringDark" x1="0" y1="0" x2="1" y2="1">
        <stop offset="0" stop-color="#f4306f"/>
        <stop offset="1" stop-color="#f7a47e"/>
      </linearGradient>
      <linearGradient id="photoDark" x1="0" y1="0" x2="1" y2="1">
        <stop offset="0" stop-color="#c79a84"/>
        <stop offset="0.55" stop-color="#1d1d1d"/>
        <stop offset="1" stop-color="#9c7a69"/>
      </linearGradient>
    </defs>
    <polygon points="360,0 509,0 509,366 420,366" fill="#141414"/>
    <polygon points="330,0 342,0 300,70 288,70" fill="#ffffff"/>
    <polygon points="348,0 356,0 314,70 306,70" fill="#ffffff"/>
    <polygon points="420,366 432,366 470,300 458,300" fill="#ffffff"/>
    <polygon points="440,366 448,366 486,300 478,300" fill="#ffffff"/>
    <circle cx="322" cy="262" r="122" fill="#b9b9b9"/>
    <circle cx="340" cy="242" r="126" fill="none" stroke="url(#ringDark)" stroke-width="6"/>
    <circle cx="340" cy="242" r="112" fill="url(#photoDark)" role="img" aria-label="Close-up photo of a hand holding a black body trimmer"/>
    <circle cx="193" cy="283" r="7" fill="#f4306f"/>
    <circle cx="218" cy="2" r="9" fill="#f7a47e"/>
    <circle cx="6" cy="358" r="8" fill="#f4306f"/>
  </svg>
  <div class="brand">
    <p class="brand__name">LustPrep.com</p>
    <p class="brand__tagline">Set for whatever...</p>
  </div>
  <a class="cta" href="#">SHOP NOW</a>
</section>

<section class="banner banner--light">
  <svg class="banner__art" width="509" height="366" viewBox="0 0 509 366">
    <defs>
      <linearGradient id="panelPink" x1="0" y1="1" x2="1" y2="0">
        <stop offset="0" stop-color="#f7a47e"/>
        <stop offset="0.5" stop-color="#f4306f"/>
        <stop offset="1" stop-color="#f4306f"/>
      </linearGradient>
      <linearGradient id="photoLight" x1="0" y1="0" x2="1" y2="1">
        <stop offset="0" stop-color="#6d4b3e"/>
        <stop offset="0.6" stop-color="#c79a84"/>
        <stop offset="1" stop-color="#e9ddd6"/>
      </linearGradient>
    </defs>
    <polygon points="360,0 509,0 509,366 395,366 420,250" fill="url(#panelPink)"/>
    <polygon points="150,366 509,366 509,150" fill="url(#panelPink)" opacity="0.85"/>
    <circle cx="415" cy="61" r="57" fill="#ffffff"/>
    <circle cx="415" cy="61" r="52" fill="url(#photoLight)" role="img" aria-label="Close-up photo of a trimmer held against the body"/>
    <circle cx="351" cy="249" r="108" fill="#ffffff"/>
    <circle cx="351" cy="249" r="103" fill="url(#photoLight)" role="img" aria-label="Close-up photo of a hand using a white trimmer"/>
  </svg>
  <div class="brand">
    <p class="brand__name">LustPrep.com</p>
    <p class="brand__tagline">Set for whatever...</p>
  </div>
  <div class="headline">
    <p class="headline__row"><span class="headline__key">Lorem</span><span class="headline__script">ipsum</span></p>
    <p class="headline__script">dolor sit amet</p>
  </div>
  <a class="cta" href="#">SHOP NOW</a>
</section>

</body>
</html>
```